Judicial election website to attract voters

I need a simple one-page web design for a judicial election. I'm going to put up one picture, maybe two. The picture I have needs a little touch-up (whiten teeth for example). I have 3 paragraphs of text. I'd like a "Donate" button that can link to a CoinDrift account. I'd also like a little background design, like the Constitution or something like that. There's a couple other little things but that's the bulk of it.

Target Market(s)

Involved voters and some media

Industry/Entity Type

Legal

Number of Pages Required

1 page

Font styles to use
Sans Serif

Requirements
Must have
• My picture, text, donate button
• Phrase "Remember to vote September 13, 2016!"
Nice to have
• Perhaps a second photo, maybe a short 30 second video of me talking directly to the voters, cool background: Constitution, something judgey.
Should not have
• Not sure ... profanity, I guess.

```html
<!DOCTYPE html>
<html lang="en">
<head>
<meta charset="utf-8">
<title>Marianne Louise Halvorsen for Circuit Court Judge</title>
<link rel="stylesheet" href="https://fonts.googleapis.com/css2?family=Arimo:ital,wght@0,400;0,700;1,400&family=Great+Vibes&display=swap">
<style>
  :root {
    --blue: #1a97e0;
    --blue-light: #36b9ee;
    --blue-dark: #1686dc;
    --ink: #333333;
    --body-text: #555555;
    --card: #d9d9d9;
    --footer: #262626;
    --white: #ffffff;
  }
  * { box-sizing: border-box; margin: 0; padding: 0; }
  html, body { width: 1063px; height: 1200px; overflow: hidden; }
  body { font-family: "Arimo", Arial, sans-serif; background: var(--white); position: relative; }

  .hero {
    position: absolute; left: 0; top: 0; width: 1063px; height: 637px;
    background:
      radial-gradient(ellipse at 85% 20%, rgba(120,40,40,.45), transparent 55%),
      radial-gradient(ellipse at 60% 95%, rgba(110,90,60,.55), transparent 60%),
      linear-gradient(180deg, #111 0%, #2a2420 45%, #4a3e30 100%);
  }
  .site-header { position: absolute; left: 0; top: 0; width: 1063px; height: 82px; background: rgba(0,0,0,.35); }
  .site-title {
    position: absolute; left: 76px; top: 18px;
    font-family: "Great Vibes", cursive; font-weight: 400; font-size: 38px; color: var(--white);
    white-space: nowrap;
  }
  .search-button {
    position: absolute; left: 946px; top: 18px; width: 42px; height: 42px;
    border: 2px solid var(--white); border-radius: 50%;
    display: flex; align-items: center; justify-content: center;
  }

  .slider-card {
    position: absolute; left: 76px; top: 130px; width: 911px; height: 407px;
    background: var(--card); border-radius: 6px; overflow: hidden;
  }
  .candidate-photo {
    position: absolute; left: 0; top: 0; width: 380px; height: 407px;
    background: linear-gradient(90deg, #bdbdbd 0%, #c9c9c9 70%, var(--card) 100%);
  }
  .slide-copy { position: absolute; left: 416px; top: 76px; }
  .slide-name { font-family: "Great Vibes", cursive; font-size: 62px; color: #222; line-height: 1; }
  .slide-reminder { margin-top: 12px; font-size: 26px; color: var(--blue); text-shadow: 1px 2px 3px rgba(0,0,0,.2); }
  .slide-date { margin-top: 4px; font-size: 44px; font-weight: 700; color: var(--blue); text-shadow: 2px 3px 4px rgba(0,0,0,.25); line-height: 1.1; }
  .slide-invite { margin-top: 22px; font-size: 14px; font-style: italic; color: #444; }
  .contact-button {
    display: inline-block; margin-top: 10px; width: 135px; height: 39px; line-height: 39px; text-align: center;
    background: linear-gradient(180deg, #2aa4ef, var(--blue-dark)); color: var(--white);
    font-size: 15px; font-weight: 700; border-radius: 3px; border: 1px solid #1479c4;
  }
  .slider-dots { position: absolute; left: 825px; top: 373px; display: flex; gap: 4px; }
  .slider-dots span { width: 11px; height: 11px; border: 2px solid #555; border-radius: 50%; }
  .slider-dots span.is-active { border-color: var(--blue); }

  .quality-tags { position: absolute; top: 571px; left: 0; width: 1063px; display: flex; justify-content: center; gap: 17px; }
  .quality-tag {
    width: 159px; height: 39px; line-height: 37px; text-align: center;
    border: 1px solid var(--white); border-radius: 3px; color: var(--white);
    font-size: 14px; font-weight: 700; background: rgba(0,0,0,.25);
  }

  .about { position: absolute; left: 76px; top: 664px; width: 900px; }
  .about-heading { font-size: 21px; font-weight: 700; color: var(--ink); }
  .about-heading span { color: var(--blue); }
  .about p { margin-top: 18px; font-size: 11px; line-height: 22px; color: var(--body-text); letter-spacing: -0.1px; }
  .about p + p { margin-top: 9px; }
  .about p.spaced { margin-top: 17px; }

  .campaign-band {
    position: absolute; left: 0; top: 1021px; width: 1063px; height: 107px;
    background: linear-gradient(180deg, var(--blue-light), var(--blue-dark));
  }
  .campaign-note { position: absolute; left: 76px; top: 30px; color: var(--white); font-size: 17px; line-height: 27px; }
  .campaign-note strong { font-weight: 700; }
  .donate-button {
    position: absolute; left: 826px; top: 31px; width: 160px; height: 45px; line-height: 43px; text-align: center;
    border: 2px solid var(--white); border-radius: 3px; color: var(--white); font-size: 16px; font-weight: 700;
  }

  .site-footer { position: absolute; left: 0; top: 1128px; width: 1063px; height: 72px; background: var(--footer); }
  .copyright { text-align: center; padding-top: 27px; color: #ddd; font-size: 12px; }
</style>
</head>
<body>
  <section class="hero" role="img" aria-label="Dark background of a flag draped over a historic constitution document"></section>

  <header class="site-header">
    <h1 class="site-title">Marianne Louise Halvorsen for Circuit Court Judge</h1>
    <div class="search-button" aria-label="Search">
      <svg width="14" height="14" viewBox="0 0 14 14"><circle cx="5.8" cy="5.8" r="4" fill="none" stroke="#fff" stroke-width="2.2"/><line x1="8.8" y1="8.8" x2="12.5" y2="12.5" stroke="#fff" stroke-width="2.6" stroke-linecap="round"/></svg>
    </div>
  </header>

  <div class="slider-card">
    <div class="candidate-photo" role="img" aria-label="Black and white portrait photo of the candidate smiling"></div>
    <div class="slide-copy">
      <div class="slide-name">Marianne</div>
      <div class="slide-reminder">REMEMBER TO VOTE</div>
      <div class="slide-date">SEPTEMBER 13, 2016!</div>
      <div class="slide-invite">I'd love to hear from you</div>
      <a class="contact-button">CONTACT ME</a>
    </div>
    <div class="slider-dots"><span></span><span></span><span class="is-active"></span><span></span><span></span></div>
  </div>

  <nav class="quality-tags">
    <div class="quality-tag">EXPERIENCED</div>
    <div class="quality-tag">DEDICATED</div>
    <div class="quality-tag">RESPECTED</div>
  </nav>

  <section class="about">
    <h2 class="about-heading">ABOUT <span>MARIANNE</span></h2>
    <p>Marianne was born and raised in Bayport, the daughter of an air-conditioning repairman who later opened his own successful business. As the first in her family to go to college, her parents could not have been more proud as she finished her degree at Gulf Coast University, then continued on to Northbridge University School of Law where she graduated with honors.</p>
    <p>Dedicating her life to public service in the lake region, she has spent the last 18 years as a prosecutor fighting for victims of child abuse and sexual abuse in Cedar and Willow counties. She participates in local charities such as the Harvest Table Pantry and the Open Pages Reading Circle. Marianne shares her knowledge and experience freely, often mentoring the other young prosecutors and lecturing on jury selection and trial strategies. She is also committed to ensuring ethical behavior in the profession of law. In law school, she won an award professionalism but since then she also served as Chair of a State Bar Grievance Committee, which handles complaints and ethical violations committed by local attorneys.</p>
    <p class="spaced">The cornerstone of Marianne’s candidacy for judge is her experience in the courtroom. Nobody knows how to run an efficient courtroom better than an attorney who has litigated a hundred felony jury trials and argued more pretrial motions than can be counted. But even a judge with all the right knowledge and experience cannot excel without the correct temperament. Ask any attorney or judge who has worked with Marianne and they will tell you that she treats everyone with respect and handles courtroom surprises with a calm head &amp; sense of humor. She would love your support for judge and the opportunity to use her skills and experience to serve Cedar &amp; Willow County in a new and exciting way.</p>
  </section>

  <section class="campaign-band">
    <p class="campaign-note">PAID FOR BY THE CAMPAIGN TO ELECT MARIANNE HALVORSEN FOR<br><strong>CIRCUIT JUDGE, CIRCUIT 6, GROUP 3</strong></p>
    <a class="donate-button">DONATE NOW!</a>
  </section>

  <footer class="site-footer">
    <p class="copyright">© Copy Rights 2016 Marianne.All Rights Reserved.</p>
  </footer>
</body>
</html>
```